WATER SACHET DESIGN NEEDED

I need a simple package designs for a PRODUCT for a company based in Ghana, Africa that will produce sachet (pouch) water. I already have a logo and now need a water background design for the sachet (Pouch). I do like to use blue water-like background. The package design should express pure, refreshing and healthy drinking water from a natural spring. The product is be called:”lumariva”

MEANING OF NAME: À gogo, often anglicized as A Go-Go, is a French expression meaning "in abundance, galore".
SLOGAN: LUMARIVA: Water-On-The-Go
LUMARIVA: Water-To-Go

DIMENSION OF PACKAGE: 5 inches x 5 inches

The logo will be in the center of the package.
The logo orientation on the sachet will be HORIZONTAL.
Logo Text:
“lumariva”
Natural Mineral Water
Logo Styles of Interest :
Brenosa water
Target Market:
General public
Must have:
Blue water-like background just like Brenosa example
KISS : Keep it simple stupid

Industry/Entity Type

It Company

```html
<!DOCTYPE html>
<html lang="en">
<head>
<meta charset="utf-8">
<title>lumariva – Mineral Water Sachet</title>
<link rel="stylesheet" href="https://fonts.googleapis.com/css2?family=Fira+Sans:wght@300;600&display=swap">
<style>
  :root {
    --aqua-light: #cff6f4;
    --aqua-mid: #b1eeed;
    --aqua-deep: #a3dfe0;
    --banner-red: #e8102e;
    --white: #ffffff;
  }
  html, body {
    margin: 0;
    padding: 0;
    overflow: hidden;
    background: var(--aqua-light);
  }
  .sachet {
    position: relative;
    width: 1200px;
    height: 1200px;
    overflow: hidden;
    background: var(--aqua-light);
  }
  .water-backdrop {
    position: absolute;
    inset: 0;
    background:
      radial-gradient(ellipse 420px 520px at 800px 480px, var(--aqua-deep) 0%, var(--aqua-mid) 55%, transparent 80%),
      radial-gradient(ellipse 520px 300px at 560px 960px, var(--aqua-deep) 0%, var(--aqua-mid) 50%, transparent 80%),
      radial-gradient(circle 110px at 235px 235px, var(--aqua-mid) 0%, transparent 100%),
      var(--aqua-light);
  }
  .banner {
    position: absolute;
    inset: 0;
    width: 1200px;
    height: 1200px;
  }
  .brand {
    position: absolute;
    left: 0;
    width: 1200px;
    top: 500px;
    text-align: center;
    margin: 0;
    padding-left: 20px;
    box-sizing: border-box;
    font-family: "Fira Sans", sans-serif;
    font-weight: 600;
    font-size: 190px;
    line-height: 1;
    letter-spacing: 20px;
    color: var(--white);
  }
  .descriptor {
    position: absolute;
    right: 155px;
    top: 675px;
    margin: 0;
    font-family: "Fira Sans", sans-serif;
    font-weight: 300;
    font-size: 33px;
    letter-spacing: 0.5px;
    color: var(--white);
  }
</style>
</head>
<body>
  <main class="sachet">
    <div class="water-backdrop" role="img" aria-label="Soft aqua water splash with swirling waves, droplets and bubbles"></div>

    <svg class="banner" viewBox="0 0 1200 1200" aria-hidden="true">
      <path fill="var(--banner-red)"
        d="M28 333 Q600 540 1175 345 L1175 900 Q600 700 28 912 Z"/>
      <path fill="none" stroke="var(--white)" stroke-width="7"
        d="M28 412 Q520 560 1090 375"/>
      <path fill="none" stroke="var(--white)" stroke-width="7"
        d="M28 830 Q520 660 1175 908"/>
    </svg>

    <h1 class="brand">lumariva</h1>
    <p class="descriptor">MINERAL WATER</p>
  </main>
</body>
</html>
```